Develop new wine label for entry level Greek wines **

We need a label design for the new line of entry level Greek wines.

We will have 4 SKU: red dry wine, red semi sweet wine, white dry wine, white semi-sweet wines.

We would like to see traditional greek houses on it.

There needs to be a slight colour difference between dry and semi sweet wines (you can maybe change colours of some details in order to differentiate wines on the shelf).

We would like to use designs that use white and blue colours (I attached some images for your inspiration). The glass bottle will be transparent so keep in mind how the label will coordinate with the colour of the wine itself.

The label needs to communicate that the wine is from Greece, this wine is simple, approachable, easy to drink, modern and fun.

The brand name is the ancient Greek word "velmara". Quoting knowlia: " Velmara (ancient Greek: βέλμαρα, plural: βέλμαρες; English prefix: eco- for ecology and economics) refers to three related but distinct concepts: the family, the family's property, and the house.".

So feel free to further elaborate on the concept.

The text that should appear on the label:
1. Brand name - Velmara (a good idea would be to use a greek style shrift would be great to mimic greek letters βέλμαρα).
2. White semi-sweet / White dry / Red semi-sweet / Red dry

Target Market(s)

Ukraine

Font styles to use
Serif

Colors
33a6d7
cee9f5
ffffff
e34297

Requirements
Must have
• The customer needs to look at the bottle and understand that is it from Greece straight away.

```html
<!DOCTYPE html>
<html lang="en">
<head>
<meta charset="utf-8">
<title>Velmara – Semi-Sweet Labels</title>
<link rel="stylesheet" href="https://fonts.googleapis.com/css2?family=Jost:wght@400;500&display=swap">
<style>
  :root {
    --backdrop: #f3f3f3;
    --label-paper: #ffffff;
    --splash-light: #cee9f5;
    --splash-mid: #8ccbea;
    --splash-deep: #33a6d7;
    --house-navy: #2e3a8c;
    --house-grey: #8e96a3;
    --ink-navy: #2b2f6b;
    --ink-blue: #3a5aa8;
    --ink-soft: #7eaedc;
  }
  * { box-sizing: border-box; margin: 0; padding: 0; }
  html, body {
    width: 1000px;
    height: 1200px;
    overflow: hidden;
    background: var(--backdrop);
  }
  .label-sheet {
    width: 1000px;
    height: 1200px;
    display: flex;
    justify-content: center;
    align-items: center;
    gap: 50px;
  }
  .wine-label {
    position: relative;
    width: 440px;
    height: 540px;
    background: var(--label-paper);
    box-shadow: 0 2px 10px rgba(0, 0, 0, 0.08);
    font-family: "Jost", sans-serif;
  }
  .watercolor-splash {
    position: absolute;
    left: 30px;
    top: 40px;
    width: 380px;
    height: 310px;
    border-radius: 46% 40% 44% 38% / 30% 36% 32% 40%;
    background: radial-gradient(ellipse at 50% 40%, var(--splash-mid) 0%, var(--splash-light) 85%);
  }
  .brand-name {
    position: absolute;
    top: 62px;
    left: 0;
    width: 100%;
    text-align: center;
    font-size: 44px;
    font-weight: 400;
    letter-spacing: 3px;
    color: var(--label-paper);
  }
  .village-houses {
    position: absolute;
    left: 110px;
    top: 140px;
    width: 230px;
    height: 200px;
    background: linear-gradient(160deg, var(--house-navy) 0%, var(--house-grey) 60%, var(--ink-blue) 100%);
    border-radius: 4px 4px 0 0;
  }
  .wine-details {
    position: absolute;
    top: 388px;
    left: 0;
    width: 100%;
    text-align: center;
  }
  .wine-style {
    font-size: 25px;
    font-weight: 500;
    color: var(--ink-navy);
    letter-spacing: 0.5px;
  }
  .vintage {
    margin-top: 10px;
    font-size: 22px;
    font-weight: 500;
    color: var(--ink-blue);
  }
  .origin {
    margin-top: 10px;
    font-size: 15px;
    font-weight: 500;
    letter-spacing: 1.5px;
    color: var(--ink-soft);
  }
</style>
</head>
<body>
  <main class="label-sheet">
    <section class="wine-label wine-label--white">
      <div class="watercolor-splash" role="img" aria-label="Light blue watercolour brush splash"></div>
      <div class="village-houses" role="img" aria-label="Illustration of whitewashed Greek island houses with a blue dome"></div>
      <h1 class="brand-name">VELMARA</h1>
      <div class="wine-details">
        <p class="wine-style">SEMI-SWEET WHITE</p>
        <p class="vintage">2020</p>
        <p class="origin">WINE OF GREECE</p>
      </div>
    </section>

    <section class="wine-label wine-label--red">
      <div class="watercolor-splash" role="img" aria-label="Light blue watercolour brush splash"></div>
      <div class="village-houses" role="img" aria-label="Illustration of whitewashed Greek island houses with a blue dome"></div>
      <h1 class="brand-name">VELMARA</h1>
      <div class="wine-details">
        <p class="wine-style">SEMI-SWEET RED</p>
        <p class="vintage">2020</p>
        <p class="origin">WINE OF GREECE</p>
      </div>
    </section>
  </main>
</body>
</html>
```